Design eines privaten Leadership-Leitbildes
Zielgruppe
Es geht um mein privates Leadership-Leitbild. Ich bin CEO eines Unternehmens, das sich in der Schweiz und international intensiv mit der Digitalen Transformation im Bauwesen befasst (www.tlv-bau.ch).
Aufgabenstellung
Die Vorlage ist bereits recht konkret und beinhaltet alles. In der grafischen Aufbereitung ist der Kreative frei. Allerdings geht es um einen Business-Content und bei meinem Leadership-Leitbild um meine persönliche 'Visitenkarte'. Also nicht 'verspielt' oder 'witzig'. Das Plakat soll A4 und A3 genutzt werden und auch auf einem gängigen Laser-Drucker in guter Qualität ausgedruckt werden können.

```html
<!DOCTYPE html>
<html lang="de">
<head>
<meta charset="utf-8">
<title>Leadership-Leitbild</title>
<link href="https://fonts.googleapis.com/css2?family=Bebas+Neue&family=Open+Sans:wght@400;600&display=swap" rel="stylesheet">
<style>
  :root {
    --bg: #48494b;
    --accent: #d07a2c;
    --text: #ffffff;
  }
  html, body {
    margin: 0;
    padding: 0;
    overflow: hidden;
    background: var(--bg);
  }
  .poster {
    position: relative;
    width: 848px;
    height: 1200px;
    background: var(--bg);
    overflow: hidden;
    color: var(--text);
    font-family: "Open Sans", sans-serif;
  }
  .skyline {
    position: absolute;
    left: 0;
    top: 230px;
    width: 848px;
    height: 970px;
    background: linear-gradient(180deg, rgba(60,61,63,0) 0%, rgba(60,61,63,0.55) 35%, rgba(60,61,63,0.45) 100%);
  }
  .brand {
    position: absolute;
    top: 14px;
    right: 33px;
    display: flex;
    align-items: baseline;
    gap: 12px;
  }
  .brand-name {
    font-weight: 600;
    font-size: 44px;
    line-height: 1;
    letter-spacing: 1px;
  }
  .brand-tagline {
    font-weight: 400;
    font-size: 12.5px;
    letter-spacing: 0.5px;
  }
  .pillar {
    position: absolute;
    top: 128px;
    width: 200px;
    margin-left: -100px;
    text-align: center;
  }
  .pillar svg {
    display: block;
    margin: 0 auto;
    width: 112px;
    height: 112px;
    stroke: var(--accent);
    fill: none;
    stroke-width: 4;
    stroke-linecap: round;
    stroke-linejoin: round;
  }
  .pillar-title {
    position: absolute;
    top: 145px;
    left: 0;
    width: 200px;
    font-family: "Bebas Neue", sans-serif;
    font-size: 48px;
    line-height: 1;
  }
  .section {
    position: absolute;
    left: 92px;
    width: 720px;
  }
  .section-kicker {
    font-family: "Bebas Neue", sans-serif;
    font-size: 29px;
    line-height: 1;
    display: block;
  }
  .section-title {
    font-family: "Bebas Neue", sans-serif;
    font-size: 50px;
    line-height: 0.9;
    color: var(--accent);
    display: block;
    margin: -6px 0 0;
    font-weight: 400;
  }
  .section-text,
  .vision-text p {
    font-weight: 600;
    font-size: 16.3px;
    line-height: 18.3px;
    text-transform: uppercase;
    white-space: nowrap;
  }
  .section-text { margin: 4px 0 0; }
  .vision-text { margin-top: 5px; }
  .vision-text p { margin: 0 0 17.5px; }
</style>
</head>
<body>
<main class="poster">
  <div class="skyline" role="img" aria-label="Dezente Stadtsilhouette aus grauen Quadratrastern im Hintergrund"></div>

  <header class="brand">
    <span class="brand-name">TLV Bau</span>
    <span class="brand-tagline">Digitales Bauen</span>
  </header>

  <div class="pillar" style="left:156px">
    <svg viewBox="0 0 120 120" aria-hidden="true">
      <ellipse cx="60" cy="60" rx="38" ry="52"/>
      <ellipse cx="60" cy="60" rx="28" ry="41"/>
      <ellipse cx="60" cy="60" rx="18" ry="30"/>
      <ellipse cx="60" cy="60" rx="8" ry="18"/>
    </svg>
    <div class="pillar-title">Identität</div>
  </div>
  <div class="pillar" style="left:340px">
    <svg viewBox="0 0 120 120" aria-hidden="true">
      <path d="M38 84 C22 72 16 56 18 42 C22 18 42 6 60 6 C82 6 100 22 100 44 C100 60 92 72 82 84"/>
      <line x1="42" y1="92" x2="80" y2="92"/>
      <line x1="42" y1="102" x2="80" y2="102"/>
      <line x1="46" y1="112" x2="76" y2="112"/>
      <circle cx="58" cy="44" r="24"/>
      <circle cx="58" cy="44" r="12"/>
      <line x1="58" y1="44" x2="112" y2="44"/>
      <path d="M104 36 L114 44 L104 52"/>
    </svg>
    <div class="pillar-title">Mission</div>
  </div>
  <div class="pillar" style="left:525px">
    <svg viewBox="0 0 120 120" aria-hidden="true">
      <path d="M4 44 L28 16 L92 16 L116 44 L60 108 Z"/>
      <line x1="4" y1="44" x2="116" y2="44"/>
      <path d="M28 16 L42 44 L60 16 L78 44 L92 16"/>
      <path d="M42 44 L60 108 L78 44"/>
    </svg>
    <div class="pillar-title">Werte</div>
  </div>
  <div class="pillar" style="left:710px">
    <svg viewBox="0 0 120 120" aria-hidden="true">
      <path d="M4 62 C24 34 42 24 60 24 C80 24 98 34 116 54"/>
      <path d="M4 62 C24 88 42 96 60 96 C80 96 98 86 116 58"/>
      <circle cx="60" cy="60" r="28"/>
      <circle cx="60" cy="60" r="16"/>
    </svg>
    <div class="pillar-title">Vision</div>
  </div>

  <section class="section" style="top:377px">
    <span class="section-kicker">Mein</span>
    <h2 class="section-title">ID-Statement</h2>
    <p class="section-text" style="margin-top:-4px">Ich bin der klare Laser Richtung Freiheit!</p>
  </section>

  <section class="section" style="top:474px">
    <span class="section-kicker">Meine</span>
    <h2 class="section-title">Mission</h2>
    <p class="section-text" style="margin-top:3px">Ich fördere Menschen, die mir vertrauen, um gemeinsam Wunder gesche-<br>hen zu lassen, die uns im Herzen verbinden.</p>
  </section>

  <section class="section" style="top:600px">
    <span class="section-kicker">Meine</span>
    <h2 class="section-title">Werte</h2>
    <p class="section-text">Authentizität, Integrität, Gestalten, Begeisterung, Verantwortung, Men-<br>schlichkeit, Empathie, Klarheit, Transparenz, Weisheit, Weitblick, Erfolg</p>
  </section>

  <section class="section" style="top:725px">
    <span class="section-kicker">Meine</span>
    <h2 class="section-title">Vision</h2>
    <div class="vision-text">
      <p>Ich vertraue den Mitarbeitenden und bin offen. Offenheit meint dabei<br>sowohl den offenen Umgang mit Informationen, als auch die Offenheit<br>für Neues und die Freude am Experimentieren.</p>
      <p>Ich begegne allen Mitarbeitenden auf Augenhöhe. Visionen und Ziele<br>werden gemeinsam entwickelt. Es zählen die besten Argumente und Ideen,<br>keine anderen Faktoren wie Position, Alter, Geschlecht oder Herkunft.</p>
      <p>Ich begleite und fördere meine Mitarbeitenden. Dazu schaffe ich die not-<br>wendigen Räume und Möglichkeiten: Ich gestalte damit den Rahmen und<br>die Struktur für höchste «Performance», und lasse den Mitarbeitenden<br>maximalen Gestaltungsspielraum.</p>
      <p>Ich fördere und fordere in meiner Organisation Schnelligkeit, Agilität<br>und Flexibilität.</p>
      <p>Ich sorge dafür, dass uns in allen Aktivitäten stets das weltweit best-<br>mögliche Wissen zur Verfügung steht und baue dafür auf aktiv gelebte<br>Partnerschaften.</p>
    </div>
  </section>
</main>
</body>
</html>
```